Business Card Design Project - KLB

I am looking for a more sophisticated card design for my company,
"The Kestrel Bureau"

We are a consultancy focused on strategy and change in Associations and professional organisations.

I am a lawyer and psychologist with a PhD and so am looking for something that communicates seriousness and credibility but also quirky creative solutions for strategic problems, which is my field of speciality.

I am looking for something that is quietly spoken, rather than loud colours ('credible' and 'creative' are the two adjectives that I think of as competing here).

I particularly like an embossed card style - heavy white card with plain white or white and black or white and grey text.

The key logo image for the company is a question mark and I am open to suggestions and ideas on design.

I have attached a file that includes a couple of styles that have caught my eye and my thoughts on them. Hopefully they communicate what I'm looking for.
Updates

Thank you for all the great suggestions and designs.

I really appreciated the effort and creative energy you put into your designs. I have now closed the project after selecting a design and advising the successful designer of the card that I am happy with.

Regards

Target Market(s)

Organisations (CEO's and Boards), Governments, Legal professionals, Membership Associations and aspiring professionals.

Industry/Entity Type

Lawyer

Requirements
Must have
• The key logo element is a question mark (?) and this needs to be incorporated.

Embossed style - cut outs or other design ideas interest me too.

The attached file has a number of sample ideas and comments on each one that I like.
Should not have
• I like crisp, modern fonts (Myriads etc...) and do not like embellished fonts or Times etc...

```html
<!DOCTYPE html>
<html lang="en">
<head>
<meta charset="utf-8">
<title>Kestrel Bureau – Business Card</title>
<link rel="stylesheet" href="https://fonts.googleapis.com/css2?family=Arimo:wght@700&family=Mulish:wght@300;400&display=swap">
<style>
  :root {
    --canvas: #ffffff;
    --card-edge: #222222;
    --shade-light: #ffffff;
    --shade-mid: #c9ccca;
    --shade-dark: #878a88;
    --wordmark: #8e8e8e;
    --accent: #8b2a22;
    --ink: #1c1c1c;
    --ink-soft: #333333;
  }
  html, body {
    margin: 0;
    padding: 0;
    width: 1200px;
    height: 1200px;
    overflow: hidden;
    background: var(--canvas);
  }
  .sheet {
    position: relative;
    width: 1200px;
    height: 1200px;
  }
  .card {
    position: absolute;
    display: block;
  }
  .card--front { left: 479px; top: 323px; width: 419px; height: 239px; }
  .card--back  { left: 487px; top: 617px; width: 419px; height: 239px; }
  .card__edge { fill: none; stroke: var(--card-edge); stroke-width: 1.6; }
  .wordmark { font-family: "Arimo", Arial, sans-serif; font-weight: 700; fill: var(--wordmark); }
  .wordmark-dot { fill: var(--accent); }
  .holder-name { font-family: "Mulish", sans-serif; font-weight: 300; font-size: 17px; fill: var(--ink-soft); letter-spacing: -0.3px; }
  .holder-role { font-family: "Mulish", sans-serif; font-weight: 300; font-size: 15px; fill: var(--ink-soft); }
  .contact { font-family: "Mulish", sans-serif; font-weight: 400; font-size: 11.5px; fill: var(--ink); letter-spacing: -0.2px; }
</style>
</head>
<body>
<main class="sheet">

  <svg class="card card--front" viewBox="0 0 502 286" aria-label="Business card front">
    <defs>
      <linearGradient id="shade-front" x1="215" y1="0" x2="502" y2="0" gradientUnits="userSpaceOnUse">
        <stop offset="0" stop-color="var(--shade-light)"/>
        <stop offset="0.35" stop-color="var(--shade-mid)"/>
        <stop offset="1" stop-color="var(--shade-dark)"/>
      </linearGradient>
    </defs>
    <rect width="502" height="286" fill="var(--canvas)"/>
    <path d="M215 0 Q330 60 290 150 Q270 240 235 286 L502 286 L502 0 Z" fill="url(#shade-front)"/>
    <circle class="wordmark-dot" cx="152" cy="140" r="10"/>
    <text class="wordmark" x="172" y="150" font-size="28">Kestrel Bureau</text>
    <rect class="card__edge" x="0.8" y="0.8" width="500.4" height="284.4"/>
  </svg>

  <svg class="card card--back" viewBox="0 0 502 286" aria-label="Business card back">
    <defs>
      <linearGradient id="shade-back" x1="215" y1="0" x2="502" y2="0" gradientUnits="userSpaceOnUse">
        <stop offset="0" stop-color="var(--shade-light)"/>
        <stop offset="0.35" stop-color="var(--shade-mid)"/>
        <stop offset="1" stop-color="var(--shade-dark)"/>
      </linearGradient>
    </defs>
    <rect width="502" height="286" fill="var(--canvas)"/>
    <path d="M215 0 Q330 60 290 150 Q270 240 235 286 L502 286 L502 0 Z" fill="url(#shade-back)"/>
    <circle class="wordmark-dot" cx="68" cy="140" r="7"/>
    <text class="wordmark" x="82" y="147" font-size="19">Kestrel Bureau</text>

    <text class="holder-name" x="489" y="48" text-anchor="end">Dr. Mara Ellison</text>
    <text class="holder-role" x="489" y="70" text-anchor="end">Director</text>

    <g text-anchor="middle">
      <text class="contact" x="393" y="123">Mobile: + 61400 123 456</text>
      <text class="contact" x="393" y="139">Phone: + 612 9000 4417</text>
      <text class="contact" x="393" y="156">E-mail: mara@kestrelbureau.com.au</text>
      <text class="contact" x="396" y="183">P.O Box 3184, Lindfield West,</text>
      <text class="contact" x="396" y="200">Sydney, Australia</text>
    </g>
    <rect class="card__edge" x="0.8" y="0.8" width="500.4" height="284.4"/>
  </svg>

</main>
</body>
</html>
```